VERANDOLA - Mother Daughter Piano Duo

My mom and I are performing concert pianists and are arranging (covering) classical piano music for 2 pianists (2 piano songs and also one piano-four hand songs). We need a design for the cover of our single songs and books that we produce. We will be selling our music on our website and will have links to our website store in our ClipHarbor video descriptions. Some of the composers we are arranging music for currently are Kelbrun, Wastel, Gorvk, Menki, Tolvik, Peslin and Vostrelikova. Piano music standard size is 9 x 12 inches. Our spine width will probably be 1/4 inch thick but not more than 1/2 inch.

Target Market(s)

Classical pianists, musicians and teachers

Industry/Entity Type

Clipharbor

Font styles to use
Script

Colors

Designer to choose colors to be used in the design.

Requirements
Must have
• Must have our name “VERANDOLA Mother-Daughter Piano Duo”
Nice to have
• Music symbols or piano designs.

```html
<!DOCTYPE html>
<html lang="en">
<head>
<meta charset="utf-8">
<title>VERANDOLA Mother-Daughter Piano Duo – Cover Spread</title>
<link rel="stylesheet" href="https://fonts.googleapis.com/css2?family=Cormorant+Garamond:ital,wght@1,500&family=Crimson+Text:ital,wght@0,400;1,400&display=swap">
<style>
  :root {
    --backdrop: #ecebe6;
    --ink-light: #ffffff;
    --ink-soft: #f4f1ec;
    --tone-dark: #5d5650;
    --tone-mid: #8d857d;
    --tone-warm: #b39e80;
    --tone-pale: #c9c2ba;
    --tone-gold: #c8a978;
    --placeholder: #f6f6f6;
  }
  html, body {
    margin: 0;
    width: 1200px;
    height: 837px;
    overflow: hidden;
    background: var(--backdrop);
  }
  .spread {
    position: relative;
    width: 1200px;
    height: 837px;
  }
  .cover {
    position: absolute;
    top: 175px;
    width: 345px;
    height: 458px;
    overflow: hidden;
    color: var(--ink-light);
    font-family: "Crimson Text", Georgia, serif;
  }
  .cover--back { left: 208px; }
  .cover--front { left: 648px; }

  .cover__art {
    position: absolute;
    inset: 0;
  }
  .cover--back .cover__art {
    background:
      radial-gradient(ellipse 60% 35% at 30% 12%, rgba(200,169,120,.55), transparent 70%),
      radial-gradient(ellipse 70% 30% at 50% 62%, rgba(40,36,34,.55), transparent 75%),
      radial-gradient(ellipse 60% 40% at 70% 85%, rgba(201,194,186,.6), transparent 70%),
      linear-gradient(180deg, var(--tone-mid) 0%, var(--tone-warm) 30%, var(--tone-dark) 55%, var(--tone-mid) 75%, var(--tone-pale) 100%);
  }
  .cover--front .cover__art {
    background:
      radial-gradient(ellipse 25% 45% at 45% 60%, rgba(240,236,230,.55), transparent 75%),
      radial-gradient(ellipse 30% 25% at 12% 55%, rgba(30,28,28,.6), transparent 75%),
      radial-gradient(ellipse 45% 35% at 85% 20%, rgba(214,210,206,.75), transparent 75%),
      radial-gradient(ellipse 40% 30% at 70% 70%, rgba(200,169,120,.5), transparent 75%),
      linear-gradient(180deg, var(--tone-mid) 0%, var(--tone-warm) 45%, var(--tone-gold) 70%, var(--tone-pale) 100%);
  }

  .back__heading {
    position: absolute;
    left: 21px;
    top: 20px;
    margin: 0;
    font-family: "Cormorant Garamond", "Times New Roman", serif;
    font-style: italic;
    font-weight: 500;
    font-size: 14.5px;
    letter-spacing: .2px;
    color: var(--ink-light);
  }
  .back__copy {
    position: absolute;
    left: 21px;
    width: 298px;
    margin: 0;
    font-size: 9.3px;
    line-height: 10.4px;
    color: var(--ink-soft);
  }
  .back__copy--intro { top: 54px; }
  .back__copy--detail { top: 202px; }
  .back__feature {
    position: absolute;
    left: 22px;
    top: 311px;
    width: 300px;
    display: flex;
    gap: 8px;
  }
  .back__feature-photo {
    flex: 0 0 47px;
    height: 44px;
    background: var(--placeholder);
  }
  .back__feature .back__copy {
    position: static;
    width: auto;
  }

  .front__title {
    position: absolute;
    left: 0;
    right: 0;
    top: 280px;
    margin: 0;
    text-align: center;
    font-family: "Cormorant Garamond", "Times New Roman", serif;
    font-style: italic;
    font-weight: 500;
    line-height: 1;
  }
  .front__name {
    display: block;
    font-size: 40px;
    letter-spacing: 1px;
    padding-left: 2px;
  }
  .front__tagline {
    display: block;
    margin-top: 6px;
    font-size: 17px;
    padding-left: 4px;
  }
  .front__author {
    position: absolute;
    left: 0;
    right: 0;
    top: 430px;
    margin: 0;
    text-align: center;
    font-size: 16px;
    padding-left: 2px;
  }
</style>
</head>
<body>
<main class="spread">
  <section class="cover cover--back" aria-label="Back cover">
    <div class="cover__art" role="img" aria-label="Soft faded photograph of a grand piano in an elegant room"></div>
    <h2 class="back__heading">VERANDOLA Mother-Daughter Piano Duo</h2>
    <p class="back__copy back__copy--intro">Lorem ipsum dolor sit amet, consectetur adipiscing elit, sed do eiusmod tempor incididunt ut labore et dolore magna aliqua. Placerat in egestas erat imperdiet sed euismod. Feugiat vivamus at augue eget arcu dictum varius duis. Fringilla urna porttitor rhoncus dolor. Diam quam nulla porttitor massa id neque. Diam vel quam elementum pulvinar etiam. Lorem dolor sed viverra ipsum nunc aliquet. Accumsan sit amet nulla facilisi morbi tempus. Malesuada fames ac turpis egestas maecenas pharetra. Nec sagittis aliquam malesuada bibendum arcu. Quam vulputate dignissim suspendisse in est ante in. In tellus integer feugiat scelerisque varius morbi. Varius sit amet mattis vulputate enim. Neque vitae tempus quam pellentesque nec nam aliquam sem et. In mollis nunc sed id semper. Iaculis urna id volutpat lacus laoreet non.</p>
    <p class="back__copy back__copy--detail">Ut sem viverra aliquet eget. Risus pretium quam vulputate dignissim. Quam viverra orci sagittis eu volutpat odio facilisis mauris sit. Diam quam nulla porttitor massa id neque aliquam. Venenatis tellus in metus vulputate eu scelerisque felis imperdiet proin. Quam lacus suspendisse faucibus interdum posuere lorem ipsum. Eget velit aliquet sagittis id consectetur purus ut faucibus. At imperdiet dui non. Ut eu sem integer vitae justo eget magna. Phasellus faucibus scelerisque eleifend donec pretium vulputate sapien nec.</p>
    <div class="back__feature">
      <div class="back__feature-photo" role="img" aria-label="Photo placeholder"></div>
      <p class="back__copy">Nunc id cursus metus aliquam eleifend mi in. Integer feugiat scelerisque varius morbi. Ut venenatis tellus in metus vulputate eu. Augue interdum velit euismod in pellentesque. At auctor urna nunc id cursus. In nibh mauris cursus mattis molestie a iaculis at erat. Suspendisse in est ante in nibh. Nam at lectus urna duis convallis convallis tellus. Sed risus ultricies tristique nulla aliquet enim tortor. At tempor commodo ullamcorper a. Egestas sed tempus urna et. Ut enim blandit volutpat maecenas volutpat.</p>
    </div>
  </section>

  <section class="cover cover--front" aria-label="Front cover">
    <div class="cover__art" role="img" aria-label="Soft blended photograph of a pianist in a white gown seated at a grand piano, seen from behind, overlaid with faded sheet music"></div>
    <h1 class="front__title">
      <span class="front__name">VERANDOLA</span>
      <span class="front__tagline">Mother-Daughter Piano Duo</span>
    </h1>
    <p class="front__author">Author Name</p>
  </section>
</main>
</body>
</html>
```